Pell Hartwick - Magazine

Our client would like a magazine designed for a conceptual novelty based on unconventional views on contemporary issues, including; finance, religion, politics etc.!

The novelty includes 1 main article, supporting images and 12 short poems.
We would like the designer to create page vectors, borders, fonts and other layout design elements.

In the first stage of the competition we request:

Magazine layout - 6 pages( 4 article variations based on article content and 2 poem page designs)

We would like to see high impact, striking vectors and design concepts to compliment the article content. See attached bullet point guide to article to help design page themes.

COMPANY INFO
Writer, poet, researcher and commentator. Our client is interested in sharing art and issues he believes in. Our client would like to design one magazine issue first but has a collection of material to produce a series of magazines in the future. So he is looking to establish a potentially long-term partnership with designer(s).

Target Market(s)

Quick and easy to read, coffee time magazine. Target Market: Male 40yrs+, Intellectual, Open Minded.

Industry/Entity Type

Finance

Font styles to use
Serif
Decorative

Requirements
Must have
• Main Article and Poetry: Space for 1 -2 images per page.
A subtle design feature that connects each page.
Primary colors: Jade Green and some Grayscale.
Secondary Colors: 3rd and 4th color open to designers preference.
Page Dimensions : 7.5in height, 7in width.
Articles: Same color theme, different layout and vector choice, same font color and size.
Poetry: Some design creative freedom. Focus on creating a unique title font incorporating the theme of the poem, Poetry TITLE font must be made a feature design element (poem identity)
Font: See Veldtrove Quarterly magazine styling
Columns: Single or multiple.
All vectors and images should be sourced from pixel quarry.
Nice to have
• Images/pictures that connect with article topic and align with color theme.
Should not have
• Avoid repetition of page design. To do this follow the idea of each paragraph (see attached breakdown)

```html
<!DOCTYPE html>
<html lang="en">
<head>
<meta charset="utf-8">
<title>Pell Hartwick – Health spread</title>
<link rel="stylesheet" href="https://fonts.googleapis.com/css2?family=Arvo:wght@400;700&family=Crimson+Text:ital,wght@0,400;1,400;1,600&display=swap">
<style>
  :root{
    --jade:#0f8a5f;
    --jade-dark:#0a6a48;
    --jade-light:#47b487;
    --ink-blue:#1d5ea9;
    --paper:#ffffff;
    --backdrop:#e6e6e6;
    --page-shade:#f3f3f3;
  }
  *{box-sizing:border-box;margin:0;padding:0}
  html,body{width:1200px;height:572px;overflow:hidden}
  body{background:var(--backdrop);position:relative;font-family:"Crimson Text",Georgia,serif}

  .page{position:absolute;top:16px;width:504px;height:540px;background:var(--paper);overflow:hidden}
  .page--left{left:96px;background:linear-gradient(to right,var(--paper) 88%,var(--page-shade))}
  .page--right{left:600px;background:linear-gradient(to left,var(--paper) 88%,var(--page-shade))}

  .section-band{position:absolute;top:10px;left:0;right:0;height:14px;background:var(--jade);border-bottom:2px solid var(--jade-light)}
  .section-label{position:absolute;top:1px;font-family:"Arvo",Georgia,serif;font-weight:700;font-size:9px;letter-spacing:.5px;color:#fff}
  .page--left .section-label{left:22px}
  .page--right .section-label{right:22px}

  .folio-band{position:absolute;bottom:10px;left:0;right:0;height:34px;background:var(--jade);border-top:3px solid var(--jade-light)}
  .folio{position:absolute;top:9px;font-family:"Crimson Text",Georgia,serif;font-style:italic;font-weight:600;font-size:11px;color:#fff;display:flex;align-items:center;gap:8px}
  .folio-num{font-style:normal;font-family:"Arvo",Georgia,serif;font-size:11px}
  .folio-rule{width:1px;height:16px;background:#fff}
  .page--left .folio{left:20px}
  .page--right .folio{right:20px}

  /* left page */
  .poem-title{position:absolute;top:38px;left:22px;right:14px;font-family:"Arvo",Georgia,serif;font-weight:700;font-size:37px;line-height:44px;color:var(--ink-blue);letter-spacing:-.3px;white-space:nowrap}
  .poem-art{position:absolute;top:100px;left:22px;width:218px;height:174px;border:2px solid var(--ink-blue);border-radius:12px;padding:8px}
  .poem-art-fill{width:100%;height:100%;border-radius:6px;background:linear-gradient(90deg,#cfdcef 0%,#e9eef6 50%,#f6d3d4 100%)}

  .verse{position:absolute;font-style:italic;font-size:10.5px;line-height:13px}
  .verse p{margin-bottom:9px}
  .verse--blue{color:var(--ink-blue)}
  .verse--green{color:var(--jade)}
  .wry-col-a{top:290px;left:34px;width:220px}
  .wry-col-b{top:100px;left:262px;width:230px}

  /* right page */
  .equation-banner{position:absolute;top:42px;left:22px;right:22px;height:58px;background:var(--jade);display:flex;align-items:center;justify-content:center}
  .equation-title{font-family:"Arvo",Georgia,serif;font-weight:400;font-size:44px;letter-spacing:5px;color:#fff}
  .eq-col-a{top:120px;left:24px;width:230px}
  .eq-col-b{top:120px;left:262px;width:230px}
  .indent{padding-left:10px}
</style>
</head>
<body>

<section class="page page--left">
  <div class="section-band"><span class="section-label">HEALTH</span></div>

  <h1 class="poem-title">Point me at the Wry</h1>

  <div class="poem-art">
    <div class="poem-art-fill" role="img" aria-label="Illustration of a medical caduceus beside a red cross"></div>
  </div>

  <div class="verse verse--blue wry-col-a">
    <p>Hey, vamp,<br>This is Arlen J. Crump<br>I've posted my prescription quota (with stamp)<br>And I'm ringing to ask<br>For another paid trip to Cayman<br>We'll call it a Seminar For Surgeons<br>And allow the corruption to burgeon</p>
    <p>Isn't it strange<br>How little we change<br>Isn't it sad we're insane<br>Playing the game and we won't wipe their tears<br>The game we've been playing for thousands and thousands<br>and...</p>
  </div>

  <div class="verse verse--blue wry-col-b">
    <p>Swept into the pharmaceutical cartel<br>On its practice, secrets I won't tell<br>We don't mean to heal, but just grease the wheel<br>Take on the profits and fates are sealed</p>
    <p>Point me at the wry and let em' buy<br>Point me at the wry and let em' fry<br>Point me at the lie and let em' die<br>And if you survive till twenty-twenty five<br>I hope you're exceedingly frail<br>For if you are stout we'll then take you out<br>While the people around you give in</p>
    <p>Point me at the wry and let em' buy<br>Point me at the wry and let em' fry<br>Point me at the lie and let em' die</p>
    <p>Pressing for vaccines at all sides<br>Refusals we hate, and so is<br>Sitting down to eat<br>With only GMO on your plate</p>
    <p>Curing's a crime but get your chemo in time<br>We'll give you cancer but call it treatment<br>If only you knew who controls the med schools<br>Government and media are also their tools<br>Head of State will criminalize what you just ate<br>Move by move we come down to check-mate</p>
  </div>

  <div class="folio-band">
    <div class="folio"><span class="folio-num">8</span><span class="folio-rule"></span><span>Pell Hartwick</span></div>
  </div>
</section>

<section class="page page--right">
  <div class="section-band"><span class="section-label">HEALTH</span></div>

  <div class="equation-banner"><h1 class="equation-title">THE EQUATION</h1></div>

  <div class="verse verse--green eq-col-a">
    <p>Race to the finish in the biggest heist in world history<br>These events are the same, in a different chain<br>For the myth of logic while derivatives wane<br>CEOs gather for a deregulation meeting<br>Time is short and regulation is fleeting<br>The blind are deafened and the lame are made dumb<br>For that queer equation this is the sum:<br>0 + 2 = 0</p>
    <p>Before the chops, on Credit Default Swaps<br>A fork into flesh, bets they would fail<br>Everything stretched under God's great hand;<br>A mouth to the poison, an axe to a tree<br>Investors are about to lose all their money<br>Wall Street leans on their lobbying power<br>Count the Collateralized Debt on your fingers<br>CDO rate manipulation, it's the rule of thumb<br>0 + 2 = 0</p>
    <p>Day and night are like being and time<br>All housing loans have gone sub-prime<br>Questioning profits, stir the solutions</p>
  </div>

  <div class="verse verse--green eq-col-b">
    <p>In the end, for light, you must burn your conclusions<br>Halden Brothers collapse broke the silence above the hollow<br>Goldmere Banks and Merrow Lynde were sure to follow<br>Equations of sum-loving numbers soared passed doubles<br>Mortgage foreclosures blamed on the housing bubbles<br><span class="indent">0 + 2 = 0</span></p>
    <p class="indent">It may not be nice, it may not be at all<br>You may just be completely appalled<br>But if nothing is something, if to rise is to fall<br>The banks need bailouts like a corpse needs to call<br>Nonsense is better than no sense at all<br>Hail to the lies by which all truths are bounded<br>The murder is done, the structure is founded<br>Where the current is grounded its circuitry hero<br>0 + 2 = 0</p>
    <p class="indent">Central Bank Command<br>The imperial hand of Bernholt's stand<br>Central Reserve got the balls in hand<br>It's all in the vault with print-on-demand<br>But 0 + 2 = 0</p>
  </div>

  <div class="folio-band">
    <div class="folio"><span>Pell Hartwick</span><span class="folio-rule"></span><span class="folio-num">9</span></div>
  </div>
</section>

</body>
</html>
```